Business Card Design using new attached logo

We are a family run Plumbing and Heating firm looking to improve our company image with an improved business card and new logo.We are looking to keep the company colour (Blue) involved in our design

Reason: New logo added which needs to be incorporated on designs

Industry/Entity Type

Business

Contact Information for Business Card

See attachment of all info required.

Requirements
Must have
• We have just picked a new company logo which is attached.
• Could you please provide your business card designs using this logo.
• We are looking for the logo on the back as well as the front with all the info required

```html
<!DOCTYPE html>
<html lang="en">
<head>
<meta charset="utf-8">
<title>Kestrel Services – Business Card</title>
<link href="https://fonts.googleapis.com/css2?family=Open+Sans:ital,wght@0,400;0,600;0,700;1,400&display=swap" rel="stylesheet">
<style>
  :root {
    --stage: #e9e7e3;
    --card-white: #ffffff;
    --brand-blue: #1f4f9c;
    --brand-blue-dark: #163a78;
    --brand-blue-light: #3a8fd6;
    --text-grey: #4a4a4a;
    --muted-grey: #8a8a8a;
    --rule: #d6d6d6;
  }
  * { box-sizing: border-box; margin: 0; padding: 0; }
  html, body {
    width: 1200px; height: 795px; overflow: hidden;
    background: var(--stage);
    font-family: "Open Sans", Arial, sans-serif;
  }
  .stage {
    position: relative; width: 1200px; height: 795px;
    display: flex; align-items: center; justify-content: center; gap: 48px;
  }
  .card {
    position: relative; width: 520px; height: 336px;
    border-radius: 3px;
    box-shadow: 0 10px 28px rgba(0,0,0,.18);
    overflow: hidden;
  }
  /* Front */
  .card-front { background: var(--card-white); }
  .card-front .brand {
    position: absolute; left: 44px; bottom: 58px;
    font-size: 40px; font-weight: 700; color: var(--brand-blue);
    letter-spacing: 1px; line-height: 1;
  }
  .card-front .brand-sub {
    position: absolute; left: 46px; bottom: 36px;
    font-size: 15px; font-weight: 700; color: var(--brand-blue);
    letter-spacing: 7px; text-transform: uppercase;
  }
  .details {
    position: absolute; left: 250px; top: 34px; width: 250px;
  }
  .person-name { font-size: 17px; font-weight: 700; color: var(--brand-blue); }
  .person-role { font-size: 12px; color: var(--muted-grey); margin-top: 1px; }
  .divider { height: 1px; background: var(--rule); margin: 12px 0 12px -40px; }
  .address { font-size: 11.5px; color: var(--text-grey); line-height: 1.5; }
  .contact-list { list-style: none; margin-top: 6px; }
  .contact-list li {
    display: flex; align-items: center; gap: 8px;
    font-size: 11.5px; color: var(--text-grey); line-height: 1.55;
  }
  .contact-list svg { width: 11px; height: 11px; fill: var(--brand-blue); flex: none; }
  .front-edge {
    position: absolute; right: 0; top: 0; bottom: 0; width: 6px;
    background: var(--brand-blue);
  }
  /* Back */
  .card-back {
    background: radial-gradient(circle at 58% 42%, var(--brand-blue-light) 0%, var(--brand-blue) 45%, var(--brand-blue-dark) 100%);
  }
  .tagline {
    position: absolute; left: 30px; top: 26px;
    font-size: 12px; font-style: italic; color: rgba(255,255,255,.85);
  }
  .card-back .brand {
    position: absolute; left: 0; right: 0; top: 128px; text-align: center;
    font-size: 46px; font-weight: 700; color: #ffffff; letter-spacing: 1px; line-height: 1;
  }
  .card-back .brand-sub {
    position: absolute; left: 0; right: 0; top: 186px; text-align: center;
    font-size: 15px; font-weight: 700; color: #ffffff; letter-spacing: 8px; text-transform: uppercase;
  }
</style>
</head>
<body>
<main class="stage">
  <section class="card card-front" aria-label="Business card front">
    <div class="brand">KESTREL</div>
    <div class="brand-sub">Services</div>
    <div class="details">
      <div class="person-name">Daniel Hartley</div>
      <div class="person-role">Director</div>
      <div class="divider"></div>
      <p class="address">Kestrel Services Ltd<br>14 Mill Parade, Elmfield Road<br>Ashford, AS2 7LP</p>
      <ul class="contact-list">
        <li><svg viewBox="0 0 16 16"><path d="M3.5 1l3 3-1.6 1.8a9 9 0 0 0 5.3 5.3L12 9.5l3 3-2 2.5C7 15 1 9 1 3z"/></svg>020 7946 0321</li>
        <li><svg viewBox="0 0 16 16"><rect x="4" y="1" width="8" height="5"/><rect x="1" y="6" width="14" height="8" rx="1"/></svg>020 7946 0458</li>
        <li><svg viewBox="0 0 16 16"><rect x="4" y="0.5" width="8" height="15" rx="1.5"/></svg>07700900412</li>
        <li><svg viewBox="0 0 16 16"><path d="M1 3h14v10H1z M1 3l7 6 7-6" fill="none" stroke="#1f4f9c" stroke-width="1.8"/></svg>danielhartley@kestrelservicesltd.co.uk</li>
        <li><svg viewBox="0 0 16 16"><circle cx="8" cy="8" r="6.5" fill="none" stroke="#1f4f9c" stroke-width="1.5"/><path d="M1.5 8h13M8 1.5c-3 3.5-3 9.5 0 13M8 1.5c3 3.5 3 9.5 0 13" fill="none" stroke="#1f4f9c" stroke-width="1.2"/></svg>www.kestrelservicesltd.co.uk</li>
      </ul>
    </div>
    <div class="front-edge"></div>
  </section>

  <section class="card card-back" aria-label="Business card back">
    <div class="tagline">Plumbing and Heating Services</div>
    <div class="brand">KESTREL</div>
    <div class="brand-sub">Services</div>
  </section>
</main>
</body>
</html>
```